Corporate Design für ein Installationsunternehmen
Wir sind mit dem Endergebnis sehr glücklich und zufrieden! Pelle ist auf alle unsere Wünsche und Vorschläge ohne zu zögern und mit viel Geduld eingegangen und wir können seine Arbeit wärmstens empfehlen. Vielen Dank nochmal Pelle für das tolle Design.
Zielgruppe
Wir sind ein Installationsunternehmen im Bereich Gas-, Wasser- und Heizung.
Aufgabenstellung
Das Symbol des Triskele sollte im Logo kreativ integriert werden ( wir sind jedoch offen auch für andere kreative Vorschläge die uns inspirieren).
Sauber, akkurat, symmetrisch und professionell soll es rüber kommen.
Das Symbol soll Vertrauen im Kunden wecken.

```html
<!DOCTYPE html>
<html lang="de">
<head>
<meta charset="utf-8">
<title>Kalvenor – Geschäftsausstattung</title>
<link rel="stylesheet" href="https://fonts.googleapis.com/css2?family=Raleway:wght@400;500;600;700&display=swap">
<style>
  :root {
    --navy: #1f2b45;
    --paper: #ffffff;
    --ground: #e4e4e6;
    --ink: #1b1b1f;
    --muted: #55585f;
    --red: #d7262f;
    --yellow: #e2a623;
    --blue: #2f8fdc;
    --window: #ececee;
    --shadow: 0 6px 18px rgba(0,0,0,.14);
  }
  * { box-sizing: border-box; margin: 0; padding: 0; }
  html, body { width: 1200px; height: 855px; overflow: hidden; }
  body {
    background: var(--ground);
    font-family: "Raleway", Arial, sans-serif;
    color: var(--ink);
    position: relative;
  }
  .brand-name {
    font-family: "Raleway", Arial, sans-serif;
    font-weight: 700;
    letter-spacing: .08em;
    text-transform: uppercase;
    display: flex; align-items: center; gap: 8px;
  }
  .brand-dot { width: 10px; height: 10px; border-radius: 50%; background: currentColor; display: inline-block; }
  .icon { width: 10px; height: 10px; flex: none; }

  /* Business card front */
  .card-front {
    position: absolute; left: 40px; top: 110px; width: 270px; height: 164px;
    background: var(--paper); box-shadow: var(--shadow);
    display: flex; padding: 20px 18px;
  }
  .card-front .brand-name { color: var(--navy); font-size: 15px; align-self: center; width: 120px; }
  .card-details { flex: 1; text-align: right; display: flex; flex-direction: column; gap: 9px; }
  .card-person { font-weight: 700; font-size: 14px; letter-spacing: .08em; color: var(--navy); text-transform: uppercase; line-height: 1.1; }
  .card-role { font-size: 8px; font-weight: 600; letter-spacing: .1em; text-transform: uppercase; }
  .contact-line { display: flex; justify-content: flex-end; align-items: flex-start; gap: 7px; font-size: 6.5px; line-height: 1.35; }
  .card-front::after {
    content: ""; position: absolute; left: 0; right: 0; bottom: 8px; height: 3px; background: var(--navy);
  }

  /* Business card back */
  .card-back {
    position: absolute; left: 330px; top: 110px; width: 270px; height: 164px;
    background: var(--navy); box-shadow: var(--shadow); color: #fff;
    display: flex; flex-direction: column; align-items: center; justify-content: center; gap: 18px;
  }
  .card-back .brand-name { font-size: 16px; }
  .card-web { font-size: 7.5px; letter-spacing: .25em; text-transform: uppercase; }

  /* Envelope */
  .envelope {
    position: absolute; left: 40px; top: 320px; width: 560px; height: 280px;
    background: var(--paper); box-shadow: var(--shadow); overflow: hidden;
  }
  .envelope-window {
    position: absolute; right: 36px; top: 36px; width: 210px; height: 70px;
    background: var(--window); border-radius: 6px; box-shadow: inset 0 1px 3px rgba(0,0,0,.12);
  }
  .envelope-band {
    position: absolute; left: 0; right: 0; bottom: 26px; height: 44px;
    background: var(--navy); color: #fff;
    display: flex; align-items: center; gap: 26px; padding: 0 22px;
    font-size: 7px;
  }
  .envelope-band .brand-name { font-size: 15px; margin-right: 12px; }
  .envelope-band .contact-line { justify-content: flex-start; font-size: 7px; }

  /* Letterhead */
  .letterhead {
    position: absolute; left: 630px; top: 24px; width: 540px; height: 807px;
    background: var(--paper); box-shadow: var(--shadow);
    display: flex; flex-direction: column;
  }
  .letter-header {
    height: 92px; background: var(--navy); color: #fff;
    display: flex; align-items: center; justify-content: space-between; padding: 0 30px;
  }
  .letter-header .brand-name { font-size: 18px; }
  .letter-header .contacts { display: flex; flex-direction: column; gap: 4px; }
  .letter-header .contact-line { font-size: 6.5px; }
  .letter-body { padding: 92px 60px 0 60px; font-size: 8.4px; line-height: 1.45; }
  .letter-body p { margin-bottom: 16px; }
  .letter-salutation { margin-bottom: 18px !important; }
  .letter-closing { text-align: right; margin-top: 4px; }
  .signature {
    width: 120px; height: 46px; margin: 6px 0 0 auto;
    background: linear-gradient(90deg, rgba(27,27,31,.08), rgba(27,27,31,.16));
    border-radius: 4px;
  }
  .letter-footer {
    margin-top: auto; padding: 0 40px 18px;
    display: grid; grid-template-columns: 1.3fr 1fr 1.2fr; gap: 18px;
    font-size: 6px; line-height: 1.5; text-transform: uppercase; color: var(--muted);
  }
  .letter-footer dl { display: grid; grid-template-columns: 46px 1fr; }
  .footer-rule { height: 2px; background: var(--navy); margin: 0 30px 4px; }
  .footer-rule.thin { height: 1px; margin-bottom: 22px; }
</style>
</head>
<body>

<svg width="0" height="0" style="position:absolute" aria-hidden="true">
  <symbol id="icon-phone" viewBox="0 0 10 10"><path d="M2 1l2 2-1 1c.6 1.3 1.7 2.4 3 3l1-1 2 2-1.2 1.2C4.6 9 1 5.4.8 2.2z" fill="currentColor"/></symbol>
  <symbol id="icon-mail" viewBox="0 0 10 10"><rect x=".5" y="2" width="9" height="6" fill="none" stroke="currentColor"/><path d="M.5 2l4.5 3.5L9.5 2" fill="none" stroke="currentColor"/></symbol>
  <symbol id="icon-pin" viewBox="0 0 10 10"><path d="M5 .5a3.2 3.2 0 0 1 3.2 3.2C8.2 6 5 9.5 5 9.5S1.8 6 1.8 3.7A3.2 3.2 0 0 1 5 .5z" fill="currentColor"/><circle cx="5" cy="3.7" r="1.1" fill="#fff"/></symbol>
</svg>

<section class="card-front" aria-label="Visitenkarte Vorderseite">
  <div class="brand-name"><span class="brand-dot"></span>Kalvenor</div>
  <div class="card-details">
    <div>
      <div class="card-person">Jonas Verholt</div>
      <div class="card-role">Co - Founder</div>
    </div>
    <div class="contact-line"><span>+49 4120 558 317</span><svg class="icon" style="color:var(--red)"><use href="#icon-phone"/></svg></div>
    <div class="contact-line"><span>jverholt@kalvenor.com</span><svg class="icon" style="color:var(--yellow)"><use href="#icon-mail"/></svg></div>
    <div class="contact-line"><span>Kalvenor Technik GmbH<br>12 Lindenhof Allee, Norderwen<br>Hamburg</span><svg class="icon" style="color:var(--blue)"><use href="#icon-pin"/></svg></div>
  </div>
</section>

<section class="card-back" aria-label="Visitenkarte Rückseite">
  <div class="brand-name"><span class="brand-dot"></span>Kalvenor</div>
  <div class="card-web">www.kalvenor.com</div>
</section>

<section class="envelope" aria-label="Briefumschlag">
  <div class="envelope-window"></div>
  <div class="envelope-band">
    <div class="brand-name">Kalvenor</div>
    <div class="contact-line"><svg class="icon"><use href="#icon-phone"/></svg><span>+49 4120 558 317</span></div>
    <div class="contact-line"><svg class="icon"><use href="#icon-mail"/></svg><span>jverholt@kalvenor.com</span></div>
    <div class="contact-line"><svg class="icon"><use href="#icon-pin"/></svg><span>12 Lindenhof Allee, Norderwen<br>Hamburg</span></div>
  </div>
</section>

<article class="letterhead" aria-label="Briefbogen">
  <header class="letter-header">
    <div class="brand-name"><span class="brand-dot"></span>Kalvenor</div>
    <div class="contacts">
      <div class="contact-line"><span>+49 4120 558 317</span><svg class="icon"><use href="#icon-phone"/></svg></div>
      <div class="contact-line"><span>jverholt@kalvenor.com</span><svg class="icon"><use href="#icon-mail"/></svg></div>
      <div class="contact-line"><span>Kalvenor Technik GmbH<br>12 Lindenhof Allee, Norderwen<br>Hamburg</span><svg class="icon"><use href="#icon-pin"/></svg></div>
    </div>
  </header>

  <div class="letter-body">
    <p class="letter-salutation">Dear Sir/ Madam,</p>
    <p>Kalvenor Gas Wasser Heizung Kalvenor Gas Wasser Heizung Kalvenor Gas Wasser Heizung Das Describe what your company or organization does. Who is your target-audience?</p>
    <p>Kalvenor Gas Wasser Heizung Kalvenor Gas Wasser Heizung Kalvenor Gas Wasser Heizung Das Describe what your company or organization does. Who is your target-audience? Wir sind ein Installationsunternehmen im Bereich Gas-, Wasser- und Heizung. Das Symbol des Triskele sollte im Logo kreativ integriert werden (wir sind jedoch offen auch für andere kreative Vorschläge die uns inspirieren). Sauber, akkurat, symmetrisch und professionell soll es rüber kommen. Das Symbol soll Vertrauen im Kunden wecken.</p>
    <p>Kalvenor Gas Wasser Heizung Kalvenor Gas Wasser Heizung Kalvenor Gas Wasser Heizung Das Describe what your company or organization does. Who is your target-audience?</p>
    <p class="letter-closing">Your Sincerly</p>
    <div class="signature" role="img" aria-label="Handschriftliche Unterschrift J. Verholt"></div>
  </div>

  <footer class="letter-footer">
    <div>
      Kalvenor Technik GmbH<br>12 Lindenhof Allee, Norderwen<br>Hamburg<br><br>
      Geschäftsführende Gesellschafter:<br>Mira Lenhart / Dr. med. Falk Orsen<br><br>
      Ärztliche Leiterin: Mira Lenhart
    </div>
    <div>
      Elsterweg 14B<br>02631 Wendhausen<br><br>
      <dl>
        <dt>Telefon:</dt><dd>03597-18320</dd>
        <dt>Fax:</dt><dd>03597-18322</dd>
        <dt>Email:</dt><dd>info@kalvenor.de</dd>
        <dt>Web:</dt><dd>www.kalvenor.de</dd>
      </dl>
    </div>
    <div>
      Kontoverbindung:<br><br>
      Steuernummer:<br>Nordhafen Genossenschaftsbank<br>IBAN: DE41 2105 0300 0048 7712 06<br>BIC: NORHDEXX
    </div>
  </footer>
  <div class="footer-rule"></div>
  <div class="footer-rule thin"></div>
</article>

</body>
</html>
```